Daily Deals Website Needs a Landing Page (Home Page will act as the landing page)

We need a landing page for a daily deals website that will act as the home page. We have attached the wire frame and logo for reference. Open to creative ideas and suggestions as long as the main elements of the wireframe are incorporated in the design. Need a very simplistic design approach like Vorplex's search page. (www.vorplex.com) . Very clean and distinct CTA's.

Target Market(s)

Customers looking for deals on everyday use items

Font styles to use
Sans Serif

Requirements
Must have
• clean design, lots of white space and strong CTA .
Nice to have
• need a clean design overall. Strong CTA
Should not have
• Cluttered look. Too many colors, keep it simple

```html
<!DOCTYPE html>
<html lang="en">
<head>
<meta charset="utf-8">
<title>Dealora – Daily Deals</title>
<link href="https://fonts.googleapis.com/css2?family=Cabin:wght@400;500;600;700&display=swap" rel="stylesheet">
<style>
  :root {
    --navy: #23349a;
    --green: #95d484;
    --mint: #f3f8f1;
    --grey-text: #7b7b7b;
    --ink: #1b1b1b;
    --white: #ffffff;
    --field-border: #d7dcef;
    --hero-tone: #e7eae3;
    --forest-tone: #2f6a3a;
    --lake-tone: #3f7d8c;
  }
  * { box-sizing: border-box; margin: 0; padding: 0; }
  html, body { width: 1200px; height: 1002px; overflow: hidden; }
  body {
    font-family: "Cabin", Arial, sans-serif;
    background: var(--white);
    position: relative;
    color: var(--ink);
  }
  .hero {
    position: absolute; left: 0; top: 0; width: 1200px; height: 221px;
  }
  .hero-photo {
    position: absolute; inset: 0;
    background: linear-gradient(180deg, #eef0ec 0%, var(--hero-tone) 100%);
  }
  .brand-name {
    position: absolute; left: 0; width: 1200px; text-align: center;
    font-weight: 700; font-size: 40px; letter-spacing: 1px; line-height: 1;
  }
  .hero .brand-name { top: 37px; color: var(--navy); }
  .tagline {
    position: absolute; left: 0; top: 90px; width: 1200px; text-align: center;
    font-size: 27px; line-height: 36px; font-weight: 600; color: var(--grey-text);
  }
  .signup-form {
    position: absolute; left: 420px; width: 360px; height: 41px;
    background: var(--white); border: 1px solid var(--field-border);
    border-radius: 21px; box-shadow: 0 2px 6px rgba(35,52,154,0.12);
  }
  .signup-form .field {
    position: absolute; left: 24px; top: 0; line-height: 39px;
    font-size: 10px; color: #6f6f6f;
  }
  .btn {
    display: inline-flex; align-items: center; justify-content: center; gap: 3px;
    background: var(--navy); color: var(--white); font-weight: 700;
    border-radius: 18px; box-shadow: 0 2px 5px rgba(29,43,133,0.3);
  }
  .signup-form .btn {
    position: absolute; right: 7px; top: 4px; width: 81px; height: 32px; font-size: 12px;
  }
  .btn svg { width: 8px; height: 8px; }
  .deal-card { position: absolute; top: 261px; width: 366px; text-align: center; }
  .deal-card.featured { left: 225px; }
  .deal-card.promoted { left: 609px; }
  .deal-photo { height: 191px; border-radius: 3px; }
  .deal-photo.forest { background: var(--forest-tone); }
  .deal-photo.lake { background: var(--lake-tone); }
  .deal-title { margin-top: 16px; font-size: 14.5px; font-weight: 600; color: var(--navy); line-height: 1.2; }
  .deal-text { margin-top: 8px; font-size: 8px; line-height: 11.5px; }
  .deal-card .btn { margin-top: 13px; width: 111px; height: 31px; font-size: 11.5px; }
  .newsletter {
    position: absolute; left: 0; top: 598px; width: 1200px; height: 166px;
    background: var(--mint); text-align: center;
  }
  .newsletter-title { margin-top: 27px; font-size: 14.5px; font-weight: 600; color: var(--navy); }
  .newsletter-text { margin-top: 8px; font-size: 8px; line-height: 11.5px; }
  .newsletter .signup-form { top: 93px; }
  .site-footer {
    position: absolute; left: 0; top: 764px; width: 1200px; height: 238px;
    background: var(--green); color: var(--white); text-align: center;
  }
  .site-footer .brand-name { top: 52px; color: var(--white); }
  .footer-about { position: absolute; left: 0; top: 110px; width: 1200px; font-size: 8px; line-height: 11.5px; }
  .footer-contact {
    position: absolute; left: 468px; top: 161px; width: 264px; text-align: left;
    font-size: 10px; line-height: 12px;
  }
  .footer-rule { position: absolute; left: 468px; top: 197px; width: 264px; height: 1px; background: rgba(255,255,255,0.45); }
  .copyright { position: absolute; left: 0; top: 208px; width: 1200px; font-size: 8.5px; }
</style>
</head>
<body>
  <header class="hero">
    <div class="hero-photo" role="img" aria-label="Misty mountain landscape photo"></div>
    <div class="brand-name">DEALORA</div>
    <h1 class="tagline">This is your tagline here</h1>
    <form class="signup-form" style="top:141px">
      <span class="field">Insert your email here to recived more promotion</span>
      <span class="btn">Sign Up
        <svg viewBox="0 0 10 10" fill="none" stroke="#fff" stroke-width="1.4"><path d="M1 1l4 4-4 4M5 1l4 4-4 4"/></svg>
      </span>
    </form>
  </header>

  <article class="deal-card featured">
    <div class="deal-photo forest" role="img" aria-label="Featured deal photo: aerial view of forest by the water"></div>
    <h2 class="deal-title">Featured Deal of the Day</h2>
    <p class="deal-text">Lorem ipsum dolor sit amet, consetetur sadipscing elitr, sed diam<br>nonumy eirmod tempor invidunt ut labore et.</p>
    <span class="btn">Find out more
      <svg viewBox="0 0 10 10" fill="none" stroke="#fff" stroke-width="1.4"><path d="M1 1l4 4-4 4M5 1l4 4-4 4"/></svg>
    </span>
  </article>

  <article class="deal-card promoted">
    <div class="deal-photo lake" role="img" aria-label="Promoted deal photo: mountain lake surrounded by pine forest"></div>
    <h2 class="deal-title">Promoted Deal of the Day</h2>
    <p class="deal-text">Lorem ipsum dolor sit amet, consetetur sadipscing elitr, sed diam<br>nonumy eirmod tempor invidunt ut labore et.</p>
    <span class="btn">Find out more
      <svg viewBox="0 0 10 10" fill="none" stroke="#fff" stroke-width="1.4"><path d="M1 1l4 4-4 4M5 1l4 4-4 4"/></svg>
    </span>
  </article>

  <section class="newsletter">
    <h2 class="newsletter-title">Sign up to receive exclusive finds and deals</h2>
    <p class="newsletter-text">Lorem ipsum dolor sit amet, consetetur sadipscing elitr, sed diam<br>nonumy eirmod tempor invidunt ut labore et.</p>
    <form class="signup-form">
      <span class="field">Insert your email here to recived more promotion</span>
      <span class="btn">Sign Up
        <svg viewBox="0 0 10 10" fill="none" stroke="#fff" stroke-width="1.4"><path d="M1 1l4 4-4 4M5 1l4 4-4 4"/></svg>
      </span>
    </form>
  </section>

  <footer class="site-footer">
    <div class="brand-name">DEALORA</div>
    <p class="footer-about">Lorem ipsum dolor sit amet, consetetur sadipscing elitr, sed diam<br>nonumy eirmod tempor invidunt ut labore et dolore.</p>
    <p class="footer-contact">Adress: Lorem ipsum dolor sit amet, consetetur sadipscing elitr.<br>Hotline: 0198-765-432 | Cell phone: 345-678-901</p>
    <div class="footer-rule"></div>
    <p class="copyright">© 2021 | Copyright</p>
  </footer>
</body>
</html>
```